PathVerdanta: Course with Coaching for Next Generation Leaders - needs brochure designer!

We need a brief, beautiful brochure to share a new solution for students and career transitioners struggling with the changing economy of "jobs"....Our enterprise is trademarked as PathVerdanta (which is derived from the notion of Careers in a changing "Ecosystem" globally as well as locally....)We are developing an online collaboration course platform to support students, career transitioners and changemakers! There are 4 phases in a process that extends over 1 year, with interactive coaching and mentoring throughout the process. We emphasize the combined offering of "course, coaching, community"... The community component will feature collaborative exchange around large global issues with focus in sustainable development goals i.e. food, water, energy, health, technology, entrepreneurship... Success stories of next generation leaders in action will be featured via the continuous blog and also support microblog/ facebook/ social media community building and marketing channels. So the design needed will pitch multiple values from individual to community benefits, local to global...economic, environment & "equity" or education or social...you get the idea! We have a website started that you can view....http://www.pathverdanta.example

Target Market(s)

High School, College, University, Graduate, Early Career/ Career Transitioners with focus on "sustainability" issues - interested in developing expanded collaboration across discipline areas to foster more opportunities for learning, experiential projects, jobs, mentors, etc.

Industry/Entity Type

Education

Font styles to use
Sans Serif

Colors
0355a3
00a990
abd037
0792cd

Requirements
Must have
• 4 phases represented to outline process:
• Clarify, Communicate, Collaborate, Create!
• maybe a new infographic?
• must illustrate that the process moves from "all alone" individualism to coaching partner, to "Board of Advisors" and team projects...to empowered creativity with partners - locally and globally.
• Must show collaboration involves existing leaders & next generation working together - in the field, but also in professional contexts (that look like they are not just volunteers ha ha)
• Some way to show "on the ground experience" combined with "global perspective" and maybe globally reaching impact or relationships?
• It's a course...there is homework....but it is for the person and there are no grades :-)
• There is a "new path" necessary for everybody to keep learning -- udpating career relevance --
• "leadership" is a whole new paradigm of human ingenuity across sectors and often grassroots community centered enterprise... rather than top down....
Nice to have
• Show that communications and collaboration happens both online & in person -
• and may involve private one to one coaching and also group exchanges.
• Show how working in a community provides creative support, resources, opportunities to find the "hidden job market" through community networks where "projects" become "accomplishments" with "references".
• Entrepreneurship for Careers --is for everyone at every age and you don't have to be "in school"....
Should not have
• boring references just to resumes- or look like an online course that you have to do alone without any recognition or relationship building.

```html
<!DOCTYPE html>
<html lang="en">
<head>
<meta charset="utf-8">
<title>PathVerdanta Brochure</title>
<link href="https://fonts.googleapis.com/css2?family=Roboto+Condensed:ital,wght@0,400;0,700;1,700&family=Lato:ital,wght@0,400;0,700;1,400;1,700&display=swap" rel="stylesheet">
<style>
:root{
  --blue:#0355a3;
  --blue-dark:#023f7c;
  --teal:#00a990;
  --green:#abd037;
  --green-deep:#7fb52e;
  --sky:#0792cd;
  --ink:#222;
  --charcoal:#2d2d2d;
  --paper:#f4f4f4;
  --stage:#d8d4cf;
}
*{margin:0;padding:0;box-sizing:border-box}
html,body{width:907px;height:1200px;overflow:hidden;background:var(--stage)}
body{position:relative;font-family:"Lato",sans-serif;color:var(--ink)}
.panel{position:absolute;width:392px;height:560px;background:linear-gradient(180deg,#fff 0%,var(--paper) 100%);overflow:hidden}
.p-tl{left:63px;top:40px}
.p-tr{left:455px;top:40px;background:linear-gradient(180deg,#f7f7f7,#e6e6e6)}
.p-bl{left:63px;top:612px}
.p-br{left:455px;top:612px}
.abs{position:absolute}
.cond{font-family:"Roboto Condensed",sans-serif}
.footer-band{position:absolute;left:0;right:0;bottom:0;height:40px;background:linear-gradient(180deg,#3a3a3a,#1f1f1f)}
.blue-band{position:absolute;left:0;right:0;background:linear-gradient(180deg,#0a64b5,var(--blue-dark))}
.small{font-size:7.4px;line-height:9.6px}
/* top-left */
.help-title{left:17px;top:44px;font-size:27px;font-weight:700;color:var(--green-deep)}
.brand-line{left:15px;top:73px;font-size:16px;font-weight:700;color:var(--blue)}
.intro{left:19px;top:98px;width:150px}
.intro b{display:block;font-size:12.5px;color:var(--blue);font-family:"Roboto Condensed",sans-serif}
.contact{left:188px;top:101px;font-size:9px;font-weight:700;line-height:12px}
.contact span{color:var(--blue)}
.coach-band{top:160px;height:48px;text-align:center;line-height:48px;font-size:13px;font-weight:700;color:var(--green)}
.coach-band span{color:#fff}
.team{left:15px;top:222px;display:grid;grid-template-columns:122px 128px 120px;row-gap:5px;font-size:8.6px}
.team li{list-style:none;position:relative;padding-left:9px}
.team li::before{content:"";position:absolute;left:0;top:3px;width:4px;height:4px;border-radius:50%;background:var(--blue)}
.friday{left:16px;top:280px;font-size:28px;font-weight:700;color:var(--green-deep)}
.calls{left:16px;top:313px;font-size:21px}
.call-box{left:20px;top:376px;width:166px;height:142px;background:linear-gradient(180deg,var(--green),var(--green-deep));border-radius:4px 4px 0 0;color:#1c2a0a;padding:12px 11px}
.call-box .time{text-align:center;font-size:15px;font-weight:700;color:#1a1a1a}
.call-box .lbl{font-size:10.5px;font-weight:700;margin-top:10px}
.call-box .num{font-size:16px;font-weight:700;color:#fff;font-family:"Roboto Condensed",sans-serif}
.call-box .url{font-size:9.5px;margin-top:12px}
.pencil-art{left:205px;top:360px;width:175px;height:150px;border-radius:6px;background:radial-gradient(circle at 50% 50%,#f7c531 0%,#f3a73a 45%,rgba(240,240,240,0) 75%)}
.phone{font-size:12px;color:#fff;letter-spacing:.5px;top:13px}
.phone svg{vertical-align:-2px;margin-right:4px}
/* top-right */
.word-cloud{left:0;top:0;width:392px;height:272px;background:linear-gradient(180deg,#f3f3f3,#dcdcdc)}
.mark{left:110px;top:70px;display:flex;align-items:center;gap:10px;font-size:24px;font-weight:700;color:var(--blue)}
.mark i{display:block;width:28px;height:28px;border-radius:50%;background:var(--teal)}
.name-band{top:272px;height:82px;text-align:center}
.name-band h1{font-family:"Roboto Condensed",sans-serif;font-size:33px;color:var(--green);margin-top:8px;letter-spacing:.5px}
.name-band p{color:#fff;font-size:13.5px;margin-top:3px}
.name-band p span{display:inline-block;width:7px;height:7px;border-radius:50%;background:var(--green);margin:0 2px 1px 4px}
.slogan{left:0;right:0;top:370px;text-align:center}
.slogan h2{font-family:"Roboto Condensed",sans-serif;font-size:25px;color:#222}
.slogan p{font-size:17px;color:#333;margin-top:2px}
.region-line{left:0;right:0;top:469px;height:4px;background:var(--green-deep)}
.region{left:35px;top:438px;width:322px;height:62px;border-radius:8px;background:linear-gradient(180deg,var(--green),var(--green-deep));text-align:center;color:#fff}
.region b{display:block;font-family:"Roboto Condensed",sans-serif;font-size:17.5px;margin-top:10px;color:#1d2a0a}
.region span{display:block;font-size:12px;letter-spacing:3px;margin-top:8px}
/* tabs */
.tab{position:absolute;height:36px;border-radius:6px;background:linear-gradient(180deg,var(--green),var(--green-deep));border:2px solid #fff;box-shadow:0 1px 3px rgba(0,0,0,.25);color:#fff;font-family:"Roboto Condensed",sans-serif;font-weight:700;font-size:20px;text-align:center;line-height:32px}
.rule{position:absolute;left:0;right:0;height:3px;background:var(--green-deep)}
/* bottom-left */
.course-intro{left:15px;top:54px;width:365px;text-align:justify}
.phase{position:absolute;display:flex;align-items:center}
.phase .ico{width:32px;height:32px;border-radius:50%;background:linear-gradient(180deg,var(--green),var(--green-deep));display:flex;align-items:center;justify-content:center;z-index:1;border:2px solid #fff}
.phase .pill{height:20px;line-height:20px;padding:0 14px 0 22px;margin-left:-14px;background:linear-gradient(180deg,#0b6ac2,var(--blue-dark));color:#fff;font-family:"Roboto Condensed",sans-serif;font-weight:700;font-size:12.5px;border-radius:0 10px 10px 0;width:104px}
.col-h{font-size:10.5px;font-weight:700;color:var(--blue);line-height:12px}
.col-t{margin-top:6px;width:170px}
.people-art{left:0;top:380px;width:392px;height:130px;background:linear-gradient(180deg,rgba(220,220,220,0),rgba(200,200,200,.7))}
.site{left:0;right:0;top:490px;text-align:center;font-size:10.5px;font-weight:700;letter-spacing:3px}
/* bottom-right */
.send-box{left:195px;top:218px;width:182px;height:58px;background:linear-gradient(180deg,var(--green),var(--green-deep));border:2px solid #fff;box-shadow:0 1px 3px rgba(0,0,0,.25);color:#fff;font-family:"Roboto Condensed",sans-serif;font-weight:700;font-size:11.5px;line-height:13px;padding:7px 6px}
.email{left:0;right:0;top:302px;text-align:center;font-size:11px;font-weight:700;letter-spacing:2.5px}
.flow{top:328px;height:66px;display:flex;align-items:center;justify-content:center;gap:10px;color:#fff;font-family:"Roboto Condensed",sans-serif;font-weight:700;font-size:15.5px}
.evolve{left:0;right:0;top:403px;height:103px;background:linear-gradient(180deg,var(--green),var(--green-deep));text-align:center;color:#fff;padding-top:10px}
.evolve h3{font-family:"Roboto Condensed",sans-serif;font-style:italic;font-size:16px;color:#16330a}
.evolve h4{font-family:"Roboto Condensed",sans-serif;font-style:italic;font-size:16px;color:#16330a;margin-top:4px}
.evolve p{font-size:11px;font-weight:700;line-height:13px}
.foot-dot{left:188px;top:10px;width:18px;height:18px;border-radius:50%;background:var(--teal)}
</style>
</head>
<body>

<!-- Panel: contact & calls -->
<section class="panel p-tl">
  <h2 class="abs help-title cond">MAY WE HELP YOU?</h2>
  <p class="abs brand-line cond">PATHVERDANTA</p>
  <div class="abs intro small"><b>is a community of</b>Certified Coaches &amp; Professionals<br>matching Talent-to-Task<br>achieving win/wins</div>
  <p class="abs contact">Contact us for a free<br><span>introductory conference</span><br>with a coach</p>
  <div class="blue-band coach-band">EDUCATION/ CAREER/ LEADERSHIP/ LIFE <span>TRANSITIONS COACHING</span></div>
  <ul class="abs team">
    <li>Dana Whitfield</li><li>Leadership</li><li>Coach Nora Delgado</li>
    <li>Education</li><li>Career Coach Lena Marsh</li><li>Professional Recruiter</li>
    <li>Career</li><li>Co-Active Life Coach</li><li></li>
  </ul>
  <h2 class="abs friday cond">FREE FIRST FRIDAY</h2>
  <p class="abs calls">Career Conference Calls</p>
  <div class="abs call-box">
    <div class="time cond">NOON-1PM</div>
    <div class="lbl">Conference Dial-in Number:</div>
    <div class="num">(555) 014-2200</div>
    <div class="lbl" style="margin-top:2px">Participant Access Code:</div>
    <div class="num">418207#</div>
    <div class="url">www.pathverdanta.example</div>
  </div>
  <div class="abs pencil-art" role="img" aria-label="Illustration of a yellow pencil with orange step arrows"></div>
  <div class="footer-band"></div>
</section>

<!-- Panel: cover -->
<section class="panel p-tr">
  <div class="abs word-cloud" role="img" aria-label="Faint word cloud of career and learning words"></div>
  <div class="abs mark"><i></i>PathVerdanta</div>
  <div class="blue-band name-band">
    <h1>PATHVERDANTA</h1>
    <p><span></span>Education<span></span>Career<span></span>Leadership<span></span>Coaching / Programs</p>
  </div>
  <div class="abs slogan">
    <h2>Thinking Globally, Acting Locally</h2>
    <p>Partners for a Sustainable Future</p>
  </div>
  <div class="abs region-line"></div>
  <div class="abs region"><b>Washington DC Metro Region and Beyond</b><span>www.PathVerdanta.example</span></div>
  <div class="footer-band">
    <span class="abs phone" style="left:10px"><svg width="12" height="12" viewBox="0 0 12 12"><rect width="12" height="12" rx="2" fill="#abd037"/><path d="M3.5 2.5l1.5 1.5-1 1c.6 1.2 1.4 2 2.5 2.5l1-1 1.5 1.5-1 1.2C5.5 9 3 6.5 2.6 3.5z" fill="#2d2d2d"/></svg>555-010-4471</span>
    <span class="abs phone" style="right:28px"><svg width="12" height="12" viewBox="0 0 12 12"><rect width="12" height="12" rx="2" fill="#abd037"/><path d="M3.5 2.5l1.5 1.5-1 1c.6 1.2 1.4 2 2.5 2.5l1-1 1.5 1.5-1 1.2C5.5 9 3 6.5 2.6 3.5z" fill="#2d2d2d"/></svg>555-019-3382</span>
  </div>
</section>

<!-- Panel: course & coaching -->
<section class="panel p-bl">
  <div class="tab" style="left:34px;top:2px;width:326px">FOUR PHASE CAREER COURSE</div>
  <p class="abs course-intro small">Through a proven four-phase process, integrating principles of lifelong learning, career transitions, entrepreneurship, change management, and innovation, our interdisciplinary, collaborative course is designed to guide you through creative change for career, lifestyle and/or next generation leadership.</p>

  <div class="phase" style="left:15px;top:96px"><span class="ico"><svg width="16" height="12" viewBox="0 0 16 12"><path d="M1 6q7-8 14 0-7 8-14 0z" fill="none" stroke="#fff" stroke-width="1.6"/><circle cx="8" cy="6" r="2.3" fill="#fff"/></svg></span><span class="pill">CLARIFY</span></div>
  <div class="phase" style="left:234px;top:96px"><span class="ico"><svg width="16" height="14" viewBox="0 0 16 14"><path d="M2 1h12v8H7l-3 3V9H2z" fill="#fff"/></svg></span><span class="pill">COMMUNICATE</span></div>
  <div class="phase" style="left:15px;top:134px"><span class="ico"><svg width="14" height="12" viewBox="0 0 14 12"><rect x="1" y="1" width="5" height="5" fill="#fff"/><path d="M6 6L3 11" stroke="#fff" stroke-width="2"/><rect x="8" y="1" width="5" height="5" fill="#fff"/><path d="M13 6l-3 5" stroke="#fff" stroke-width="2"/></svg></span><span class="pill">COLLABORATE</span></div>
  <div class="phase" style="left:234px;top:136px"><span class="ico"><svg width="16" height="16" viewBox="0 0 16 16"><circle cx="8" cy="8" r="6" fill="none" stroke="#fff" stroke-width="1.6"/><path d="M2 8h12M8 2v12" stroke="#fff" stroke-width="1.2"/></svg></span><span class="pill">CREATE</span></div>

  <div class="rule" style="top:203px"></div>
  <div class="tab" style="left:84px;top:188px;width:226px">COACHING</div>

  <div class="abs" style="left:14px;top:244px">
    <p class="col-h">Certified Professional<br>Coaching</p>
    <p class="col-t small"><b><i>Individual, customized, affordable</i></b> coaching for <b><i>Education, Career, Life and Leadership Transitions</i></b> at varied stages of life and career challenges, to support achievement of personal and professional goals. We work with you in person, or flexibly by phone, email, video. It is simple to get started! Just contact us and we will customize affordable services and schedule adapted to your goals.</p>
  </div>
  <div class="abs" style="left:206px;top:242px">
    <p class="col-h">Career &amp; Leadership<br>Connections</p>
    <p class="col-t small"><b><i>Group Coaching</i></b> and other program offerings can help build your network, while reducing the costs of individualized coaching, to proactively achieve your goals. Professionals exchange insights on career and organizational change management using a "TeamSpark" team assessment for innovation and change, providing mutual support as a team.</p>
  </div>

  <div class="abs people-art" role="img" aria-label="Faint silhouettes of a group of professionals"></div>
  <div class="abs" style="left:14px;top:380px">
    <p class="col-h">Resumes, Covers, Interview Prep</p>
    <p class="col-t small"><b><i>Your Professional Documents are customized,</i></b> so we offer the expertise of <i>Professional Resume Writers and Executive Recruiters</i> to prepare you for <b>Interviews</b> so you may land your next job! Individualized coaching fees may vary.</p>
  </div>
  <div class="abs" style="left:206px;top:380px">
    <p class="col-h">Resumes, Covers, Interview Prep</p>
    <p class="col-t small"><b><i>Websites and Social Media Presence are a necessity</i></b> for contemporary job search, business development, and entrepreneurship. Consultants are ready to help you develop a web based <b><i>Professional Portfolio to Market YOU,</i></b> your project or start-up enterprise.</p>
  </div>
  <p class="abs site">www.PathVerdanta.example</p>
  <div class="rule" style="top:514px;height:4px"></div>
  <div class="footer-band"></div>
</section>

<!-- Panel: programs -->
<section class="panel p-br">
  <div class="tab" style="left:82px;top:20px;width:228px">PROGRAMS</div>

  <div class="abs" style="left:17px;top:74px">
    <p class="col-h">PathVerdanta Community Course</p>
    <p class="col-t small" style="width:166px;text-align:justify"><b><i>21st Century Career &amp; Leadership Development Courses</i></b> delivered online with a team of <b><i>certified coaches plus</i></b> international, interdisciplinary forum of professionals to help you get connected. We use easy, flexible technology to allow you to participate anytime, anywhere you connect to the internet! Course may be customized for varied curricula to integrate entrepreneurial motivation that supports achievement of individual, educational and/or organizational goals.</p>
  </div>
  <div class="abs" style="left:212px;top:74px">
    <p class="col-h">Workshops/Seminars/Networking</p>
    <p class="col-t small" style="width:170px"><b><i>There is really nothing like meeting in person</i></b> to combine benefits of coaching and networking with other professionals. We offer customized workshops for organizations and will help you cultivate vital networks related to your career and leadership goals. We often host regional experts for networking events on contemporary issues impacting careers and leadership from urban to rural communities.</p>
  </div>
  <div class="abs" style="left:17px;top:193px">
    <p class="col-h">Experiential/ Leadership Projects</p>
    <p class="col-t small" style="width:166px;text-align:justify"><b><i>Experience is the best teacher for our Next Generation Professionals and Leaders.</i></b> We work with top educational institutions and partner with local leaders on projects focused on sustainable solutions building. <b><i>Do you have a project that could use fresh creative energy and skill? Are you seeking a project focused in sustainability to build expertise?</i></b></p>
  </div>
  <div class="abs send-box">SIMPLY SEND YOUR LETTER OF INTEREST, PROJECT DESCRIPTION &amp;/ OR RESUME TO:</div>
  <p class="abs email">hello@pathverdanta.example</p>

  <div class="blue-band flow">
    <span>Careers</span>
    <svg width="22" height="14" viewBox="0 0 22 14"><path d="M0 4h13V0l9 7-9 7v-4H0z" fill="#abd037"/></svg>
    <span>Ecosystems</span>
    <svg width="22" height="14" viewBox="0 0 22 14"><path d="M0 4h13V0l9 7-9 7v-4H0z" fill="#abd037"/></svg>
    <span>PathVerdanta</span>
  </div>
  <div class="abs evolve">
    <h3>Contemporary Careers are Evolving</h3>
    <p>as a dynamic organic, interdependent relationship between</p>
    <h4>People, Planet &amp; Profit Partnerships</h4>
    <p>seeking to achieve sustainable solutions ensuring a better world<br>for future generations... Think Forward!</p>
  </div>
  <div class="footer-band"><span class="abs foot-dot"></span></div>
</section>

</body>
</html>
```